San Francisco Pet Care Non Profit

Business Card Design for non profit organization.
We are a mobile pet care team who supports and attends to pets whose owners are homeless. Thanks for your help and creativity.

Industry/Entity Type

Non Profit

Contact Information for Business Card

Marisol Keddy
President
2871 Larkmoor Street, #512
San Francisco, CA 94187
phone: 415-729-3846
fax: 415-781-4052
marisol@tidywagonvan.org
website: tidywagonvan.org
facebook: facebook.com/TidyWagonVan

Font styles to use
Serif
Sans Serif

Colors

Designer to choose colors to be used in the design.

Requirements
Must have
• above details and attached logo

```html
<!DOCTYPE html>
<html lang="en">
<head>
<meta charset="utf-8">
<title>TidyWagonVan Business Cards</title>
<link rel="stylesheet" href="https://fonts.googleapis.com/css2?family=Arimo:wght@400;700&display=swap">
<style>
  :root {
    --page-bg: #e9eaea;
    --card-white: #ffffff;
    --brand-blue: #3ba9dc;
    --ink: #231f20;
    --card-shadow: rgba(0, 0, 0, 0.12);
    --faint-mark: #eeeeee;
  }
  * { margin: 0; padding: 0; box-sizing: border-box; }
  html, body {
    width: 1200px; height: 900px; overflow: hidden;
    background: var(--page-bg);
    font-family: "Arimo", Arial, sans-serif;
  }
  .sheet { position: relative; width: 1200px; height: 900px; }
  .card {
    position: absolute; width: 514px; height: 297px;
    border-radius: 26px; overflow: hidden;
    box-shadow: 0 0 0 2px #dcdddd, 0 2px 6px var(--card-shadow);
  }
  .card--front-white { left: 72px; top: 137px; background: var(--card-white); }
  .card--front-circle { left: 615px; top: 137px; background: var(--brand-blue); }
  .card--front-blue { left: 72px; top: 463px; background: var(--brand-blue); }
  .card--back { left: 615px; top: 463px; background: var(--card-white); }

  .spotlight {
    position: absolute; left: 79px; top: -30px;
    width: 354px; height: 354px; border-radius: 50%;
    background: var(--card-white);
  }
  .brand-block {
    position: absolute; left: 0; right: 0; top: 48px;
    display: flex; flex-direction: column; align-items: center;
  }
  .brand-dot {
    width: 92px; height: 92px; border-radius: 50%;
    background: var(--brand-blue);
  }
  .brand-name {
    margin-top: 22px;
    font-weight: 700; font-size: 44px; line-height: 1;
    color: var(--brand-blue); letter-spacing: -0.5px;
  }
  .tagline {
    margin-top: 8px;
    font-weight: 700; font-size: 18px; color: var(--ink);
  }
  .card--front-blue .brand-dot { background: var(--card-white); }
  .card--front-blue .brand-name,
  .card--front-blue .tagline { color: var(--card-white); }

  .back-mark {
    position: absolute; left: 345px; top: 95px;
    width: 250px; height: 250px; border-radius: 50%;
    background: var(--faint-mark);
  }
  .back-header { position: absolute; left: 44px; top: 30px; display: flex; align-items: center; }
  .back-header .brand-dot { width: 68px; height: 68px; flex: none; }
  .back-header .brand-text { margin-left: 20px; display: flex; flex-direction: column; align-items: center; }
  .back-header .brand-name { margin-top: 0; font-size: 44px; }
  .back-header .tagline { margin-top: 6px; }

  .person { position: absolute; left: 52px; top: 154px; }
  .person-name { font-weight: 700; font-size: 17px; color: var(--brand-blue); }
  .person-role { margin-top: 4px; font-weight: 700; font-size: 13px; color: var(--ink); }

  .contact-list { position: absolute; left: 52px; top: 202px; list-style: none; }
  .contact-list li {
    display: flex; align-items: center; height: 16.5px;
    font-size: 13.5px; color: var(--ink);
  }
  .contact-list svg { width: 12px; height: 12px; margin-right: 8px; flex: none; fill: var(--brand-blue); }
  .address { position: absolute; left: 333px; top: 202px; font-size: 13.5px; line-height: 16.5px; color: var(--ink); font-style: normal; }
  .address .web { color: var(--brand-blue); }
</style>
</head>
<body>
<main class="sheet">

  <section class="card card--front-white">
    <div class="brand-block">
      <div class="brand-dot"></div>
      <div class="brand-name">TidyWagonVan</div>
      <div class="tagline">Mobile Pet Care Team</div>
    </div>
  </section>

  <section class="card card--front-circle">
    <div class="spotlight"></div>
    <div class="brand-block">
      <div class="brand-dot"></div>
      <div class="brand-name">TidyWagonVan</div>
      <div class="tagline">Mobile Pet Care Team</div>
    </div>
  </section>

  <section class="card card--front-blue">
    <div class="brand-block">
      <div class="brand-dot"></div>
      <div class="brand-name">TidyWagonVan</div>
      <div class="tagline">Mobile Pet Care Team</div>
    </div>
  </section>

  <section class="card card--back">
    <div class="back-mark"></div>
    <header class="back-header">
      <div class="brand-dot"></div>
      <div class="brand-text">
        <div class="brand-name">TidyWagonVan</div>
        <div class="tagline">Mobile Pet Care Team</div>
      </div>
    </header>

    <div class="person">
      <div class="person-name">Marisol Keddy</div>
      <div class="person-role">President</div>
    </div>

    <ul class="contact-list">
      <li>
        <svg viewBox="0 0 12 12" aria-hidden="true"><path d="M1 4c0-2 2-3 5-3s5 1 5 3v1H8V3.5H4V5H1z M3 6h6l2 5H1z"/></svg>
        415-729-3846
      </li>
      <li>
        <svg viewBox="0 0 12 12" aria-hidden="true"><rect x="3" y="0.5" width="6" height="3"/><rect x="0.5" y="4" width="11" height="5" rx="1"/><rect x="3" y="8" width="6" height="3.5"/></svg>
        415-781-4052
      </li>
      <li>
        <svg viewBox="0 0 12 12" aria-hidden="true"><rect x="0.5" y="2" width="11" height="8" rx="1"/><path d="M1 2.5l5 4 5-4" stroke="#fff" stroke-width="1.2" fill="none"/></svg>
        marisol@tidywagonvan.org
      </li>
      <li>
        <svg viewBox="0 0 12 12" aria-hidden="true"><rect x="0.5" y="0.5" width="11" height="11" rx="1.5"/></svg>
        /TidyWagonVan
      </li>
    </ul>

    <address class="address">
      2871 Larkmoor Street, #512<br>
      San Francisco<br>
      CA 94187<br>
      <span class="web">www.tidywagonvan.org</span>
    </address>
  </section>

</main>
</body>
</html>
```